Welcome Card Banner Desing for email suscriptors

to get involved on this task please check my site tulavendo.app
I wish for this task a welcome postal card to get subscribers for the newsletter and get a Coupon Code for discounts,
Keep in mind Velisso is a platform where customers (girls) can get any fashion high-end accessories ready to wear, to see the categories please visit our shop.

Target Market(s)

World wide people between 18-60 years old

Industry/Entity Type

Fashion

Coding

Coded - Design and coding required

Number of Pages Required

1 page

Font styles to use
Sans Serif

Colors
a64599
ffffff
ffc214
faa54b

Requirements
Must have
• Simplicity
• to get involved on this task please check my site tulavendo.app
• I wish for this task a welcome postal card to get subscribers for the newsletter and get a Coupon Code for discounts,
• Keep in mind Velisso is a platform where customers (girls) can get any fashion high-end accessories ready to wear, to see the categories please visit our shop.
Nice to have
• Field for customer fill an email or just skip the banner
Should not have
• Bad grammar

```html
<!DOCTYPE html>
<html lang="en">
<head>
<meta charset="utf-8">
<title>Velisso Welcome Postal Card</title>
<link rel="stylesheet" href="https://fonts.googleapis.com/css2?family=Poppins:wght@500;600;800&family=Raleway:wght@700;800&display=swap">
<style>
  :root {
    --board: #464646;
    --board-glow: #5a5a5a;
    --purple: #a64599;
    --purple-dark: #8e3583;
    --white: #ffffff;
    --yellow: #ffc214;
    --orange: #faa54b;
    --ink: #2a2a2a;
    --heading: #444444;
    --paper: #f2f2f2;
    --band: #dedede;
  }
  * { margin: 0; padding: 0; box-sizing: border-box; }
  html, body { width: 1200px; height: 1200px; overflow: hidden; }
  body {
    position: relative;
    background: radial-gradient(circle at 50% 50%, var(--board-glow), var(--board) 70%);
    font-family: "Poppins", sans-serif;
  }
  .side-label {
    position: absolute; left: 0; width: 1200px; text-align: center;
    color: var(--white); font-weight: 500; font-size: 16px; letter-spacing: 0.2px;
  }
  .side-label--front { top: 48px; }
  .side-label--back { top: 623px; }

  .card {
    position: absolute; left: 225px; width: 765px; height: 495px; overflow: hidden;
    box-shadow: 0 22px 45px rgba(0,0,0,0.35);
  }
  .card--front { top: 94px; background: var(--paper); }
  .card--back {
    top: 666px;
    background: linear-gradient(135deg, #e6e6e6 0%, #f7f7f7 45%, #ffffff 70%, #ececec 100%);
  }

  .card__shapes { position: absolute; inset: 0; }

  .shopper-photo {
    position: absolute; left: 0; top: 25px; width: 300px; height: 470px;
    background: linear-gradient(180deg, #e8c9b4 0%, #d9b8a2 45%, #d9557a 70%, #e9a1a6 100%);
    border-radius: 120px 120px 0 0;
  }
  .welcome-wreath {
    position: absolute; left: 205px; top: 18px; width: 190px; height: 190px; border-radius: 50%;
    background: radial-gradient(circle, #f5f5f5 45%, #b8d6c7 62%, #e9a6c4 80%, transparent 82%);
  }

  .offer {
    position: absolute; left: 410px; top: 118px; width: 355px; text-align: center;
    font-family: "Raleway", sans-serif; font-weight: 800; color: var(--white);
  }
  .offer__ornament {
    display: block; width: 70px; height: 14px; margin: 0 auto 12px;
    background: radial-gradient(ellipse, rgba(255,255,255,0.9) 30%, transparent 70%);
  }
  .offer__title { font-size: 36px; line-height: 1.1; margin-bottom: 6px; font-weight: 800; }
  .offer__line { font-size: 28px; line-height: 37px; font-weight: 800; }
  .offer__line--accent { color: var(--yellow); }

  .subscribe-button {
    position: absolute; right: 0; bottom: 0; width: 292px; height: 68px;
    background: var(--orange); border-radius: 34px 0 0 0;
    box-shadow: -6px -6px 0 var(--purple-dark);
    display: flex; align-items: center; justify-content: center;
    font-family: "Raleway", sans-serif; font-weight: 800; font-size: 24px; color: var(--ink);
    padding-left: 12px;
  }

  .brand-ring {
    position: absolute; left: 256px; top: 24px; width: 238px; height: 238px; border-radius: 50%;
    background: var(--white); border: 15px solid var(--band);
    display: flex; align-items: center; justify-content: center;
  }
  .brand-ring__name {
    font-family: "Poppins", sans-serif; font-weight: 800; font-size: 40px; color: var(--ink);
  }
  .discount {
    position: absolute; left: 0; top: 280px; width: 765px;
    display: flex; align-items: center; justify-content: center; gap: 14px;
  }
  .discount__rule { display: flex; flex-direction: column; gap: 5px; }
  .discount__rule span { display: block; height: 2px; background: var(--orange); }
  .discount__rule--left { align-items: flex-end; }
  .discount__rule--left span:nth-child(1) { width: 100px; }
  .discount__rule--left span:nth-child(2) { width: 70px; }
  .discount__rule--left span:nth-child(3) { width: 40px; }
  .discount__rule--right { align-items: flex-start; }
  .discount__rule--right span:nth-child(1) { width: 100px; }
  .discount__rule--right span:nth-child(2) { width: 70px; }
  .discount__rule--right span:nth-child(3) { width: 40px; }
  .discount__label { font-weight: 800; font-size: 36px; color: var(--heading); line-height: 1; }
  .discount__code {
    position: absolute; left: 214px; top: 345px; width: 339px; height: 65px;
    background: var(--orange); border-radius: 10px;
    display: flex; align-items: center; justify-content: center;
    font-weight: 800; font-size: 33px; color: var(--white);
  }
</style>
</head>
<body>
  <div class="side-label side-label--front">FRONT SIDE</div>
  <section class="card card--front">
    <div class="shopper-photo" role="img" aria-label="Photo of a smiling woman in sunglasses holding shopping bags"></div>
    <div class="welcome-wreath" role="img" aria-label="Hand-lettered Welcome inside a floral wreath"></div>
    <svg class="card__shapes" viewBox="0 0 612 396" preserveAspectRatio="none" aria-hidden="true">
      <path d="M395 0 L612 0 L612 396 L305 396 C255 330 250 270 285 205 Z" fill="var(--band)"/>
      <path d="M412 0 L612 0 L612 396 L322 396 C278 335 273 275 303 212 Z" fill="var(--purple)"/>
    </svg>
    <div class="offer">
      <span class="offer__ornament" role="img" aria-label="Small decorative flourish"></span>
      <h1 class="offer__title">Postal Card</h1>
      <p class="offer__line">TO GET SUBSCRIBERS</p>
      <p class="offer__line">FOR THE NEWSLETTER</p>
      <p class="offer__line offer__line--accent">&amp; GET A COUPON CODE</p>
      <p class="offer__line offer__line--accent">FOR DISCOUNTS</p>
    </div>
    <div class="subscribe-button">SUBSCRIBERS NOW</div>
  </section>

  <div class="side-label side-label--back">BACK SIDE</div>
  <section class="card card--back">
    <div class="brand-ring"><span class="brand-ring__name">Velisso</span></div>
    <div class="discount">
      <div class="discount__rule discount__rule--left"><span></span><span></span><span></span></div>
      <h2 class="discount__label">DISCOUNT CODE</h2>
      <div class="discount__rule discount__rule--right"><span></span><span></span><span></span></div>
    </div>
    <div class="discount__code">MIOVELISSO 2</div>
  </section>
</body>
</html>
```